Call Center In Need of Website Design

We are a call center that provides inbound and outbound calling & marketing services for eCommerce store. We would like to see a fun, creative, playful design that is simple.

Here are some sample design sites we like;
- https://www.velmorink.com/
- https://tonquel.io/
- https://www.brasklode.com/live-chat-software/
- https://www.quillarbe.com/

Here are some competitor sites;
- https://www.dorvenlinkage.com/
- https://www.helpwaldrix.com/

I have attached website content for your use.
Updates

Target Market(s)

eCommerce

Coding

Coded - Design and coding required

Number of Pages Required

5+ page

Font styles to use
Sans Serif

Colors

Designer to choose colors to be used in the design.

Requirements
Must have
• Must have designs for the following 5 separate pages;
• 1. Home (landing)
• - This will be were the design style really needs to show.
• - Just needs to touch on key services
• - CTA
• 2. About Us
• - Basic page for about me paragraph
• 3. Services
• - List of services with icons
• - Click on service type to expand details or hover over service icon to view popup bubble with details about that service
• 4. Pricing
• - Option to bundle 1(one) digital service plan and 1(one) call center service plan
• - Bundling adds 10% monthly discount to over all price
• - Customer does NOT have to bundle
• - FAQ
• 5. Contact Us
• - Include a capture form (name, company name, email, phone, message)
• - Contact info
• - Business hours
• When customer purchases their desired plan, then they are taken to a page where they must schedule a call with an account rep.
Nice to have
• home page animations
Should not have
• All information on Home/Landing page.

```html
<!DOCTYPE html>
<html lang="en">
<head>
<meta charset="utf-8">
<title>Corvane — Customer Care &amp; Back-Office Support</title>
<link href="https://fonts.googleapis.com/css2?family=Open+Sans:wght@400;600;700&family=Montserrat:wght@500;700&display=swap" rel="stylesheet">
<style>
:root{
  --teal:#5fbfa8;
  --slate:#4f5957;
  --slate-dark:#565f5d;
  --ink:#4a4f50;
  --text:#5d6264;
  --muted:#8a8f91;
  --line:#e3e7e9;
  --faq-bg:#f1f5f8;
  --contact-bg:#333333;
  --field-bg:#262626;
  --field-line:#3d3d3d;
  --white:#ffffff;
}
*{box-sizing:border-box;margin:0;padding:0}
html,body{width:1200px;height:2550px;overflow:hidden}
body{position:relative;background:var(--white);font-family:"Open Sans",Arial,sans-serif;color:var(--text)}
.brand{font-family:"Montserrat",Arial,sans-serif;font-weight:500;letter-spacing:4px;text-transform:uppercase;display:flex;align-items:center;gap:12px;white-space:nowrap}
.brand-dot{border:3px solid currentColor;border-radius:50%}

/* header */
.site-header{position:absolute;top:0;left:0;width:1200px;height:85px;display:flex;align-items:center;justify-content:space-between;padding:0 160px}
.site-header .brand{color:var(--teal);font-size:22px}
.site-header .brand-dot{width:30px;height:30px}
.main-nav{display:flex;align-items:center;gap:26px;font-size:13px;color:var(--ink)}
.main-nav a{color:inherit;text-decoration:none;white-space:nowrap}
.main-nav a.active{color:var(--teal)}
.main-nav .btn-login,.main-nav .btn-signup{padding:9px 22px;border-radius:3px;color:var(--white);font-size:12px}
.main-nav .btn-login{background:var(--slate);margin-left:-6px}
.main-nav .btn-signup{background:var(--teal)}

/* hero */
.hero{position:absolute;top:85px;left:0;width:1200px;height:440px;background:var(--slate-dark);overflow:hidden}
.hero-photo{position:absolute;top:0;right:0;width:650px;height:440px;background:linear-gradient(90deg,var(--slate-dark) 0%,#9aa4a8 30%,#c9d3de 60%,#dfe5ee 100%)}
.hero-content{position:absolute;left:160px;top:125px;color:var(--white)}
.hero-content .brand{font-size:32px;color:var(--white)}
.hero-content .brand-dot{width:42px;height:42px}
.hero-lead{margin-top:30px;font-size:15px;line-height:1.35;width:345px}
.hero-actions{margin-top:18px;display:flex;gap:12px}
.hero-actions span{font-size:9px;font-weight:700;text-transform:uppercase;padding:7px 13px;border-radius:2px;white-space:nowrap}
.btn-start{background:var(--teal);color:var(--white)}
.btn-more{background:var(--white);color:var(--ink)}
.hero-wave{position:absolute;left:0;bottom:0}

/* partners */
.partners{position:absolute;top:550px;left:160px;width:880px;display:flex;align-items:center;justify-content:space-between}
.partners-label{font-size:14px;font-weight:700;letter-spacing:1px;line-height:1.4;text-transform:uppercase;color:var(--ink);width:200px}
.partners-label b{color:var(--teal)}
.partner-badges{display:flex;gap:22px}
.partner-badge{width:152px;height:76px;border:1px solid #d6d6d6;background:linear-gradient(#fafafa,#ececec);display:flex;align-items:center;justify-content:center}
.partner-badge i{width:70px;height:14px;background:#9b9b9b;border-radius:2px}

/* services */
.services-title{position:absolute;top:675px;width:1200px;text-align:center;font-size:30px;font-weight:700;letter-spacing:1px;color:var(--ink)}
.services-title b{color:var(--teal)}
.services{position:absolute;top:735px;left:0;width:1200px;height:363px;border-top:1px solid var(--line);border-bottom:1px solid var(--line);display:flex}
.service{flex:1;text-align:center;padding-top:58px}
.service + .service{border-left:1px solid var(--line)}
.service-icon{height:48px;display:flex;align-items:flex-end;justify-content:center}
.service h3{margin-top:20px;font-size:31px;font-weight:400;color:var(--ink);letter-spacing:1px;white-space:nowrap}
.service p{margin:14px auto 0;width:420px;font-size:18px;line-height:1.6;letter-spacing:.3px}
.service .btn-outline{display:inline-block;margin-top:18px;padding:7px 12px;border:1px solid #888;font-size:9px;font-weight:700;color:var(--ink);white-space:nowrap}

/* faq */
.faq{position:absolute;top:1120px;left:0;width:1200px;height:713px;background:var(--faq-bg)}
.faq-scallop{position:absolute;top:-22px;left:0}
.faq h2{position:absolute;top:95px;width:1200px;text-align:center;font-size:31px;font-weight:700;letter-spacing:1.5px;color:var(--ink);text-transform:uppercase}
.faq-list{position:absolute;top:180px;left:160px;width:880px;list-style:none}
.faq-item{border-bottom:1px solid #dde2e5;height:53px;display:flex;align-items:center;justify-content:space-between;font-size:18px;font-weight:700;color:var(--ink);letter-spacing:.5px}
.faq-item .sign{font-size:20px;font-weight:400}
.faq-item.open{height:112px;flex-wrap:wrap;align-content:flex-start;padding-top:8px}
.faq-item.open p{width:880px;margin-top:14px;font-size:12px;font-weight:400;line-height:1.6;color:var(--text);letter-spacing:0}

/* contact */
.contact{position:absolute;top:1833px;left:0;width:1200px;height:607px;background:var(--contact-bg);color:var(--white);text-align:center}
.contact h2{margin-top:84px;font-family:"Montserrat",Arial,sans-serif;font-weight:700;font-size:26px}
.contact-rule{display:flex;justify-content:center;align-items:center;gap:8px;margin-top:6px}
.contact-rule i{width:24px;height:1px;background:#bbb}
.contact-rule b{width:8px;height:8px;border:1px solid #bbb;border-radius:50%}
.contact-intro{margin:8px auto 0;width:440px;font-family:Arial,sans-serif;font-size:12px;line-height:1.6;color:#eee}
.contact-form{position:absolute;top:214px;left:328px;width:540px}
.field{background:var(--field-bg);border:1px solid var(--field-line);height:37px;text-align:left;padding:9px 12px;font-family:Arial,sans-serif;font-size:11px;color:#777;margin-bottom:16px}
.field-row{display:flex;gap:12px}
.field-row .field{flex:1}
.field.message{height:152px}
.btn-send{display:inline-block;margin-top:4px;background:var(--teal);color:var(--white);font-size:11px;font-weight:700;letter-spacing:1px;padding:12px 18px;white-space:nowrap}

/* footer */
.site-footer{position:absolute;top:2440px;left:0;width:1200px;height:110px;display:flex;align-items:center;padding:0 160px}
.site-footer .brand{color:var(--ink);font-size:25px}
.site-footer .brand-dot{width:32px;height:32px;color:var(--teal)}
.copyright{margin-left:40px;padding-left:20px;border-left:1px solid var(--line);height:40px;display:flex;align-items:center;font-size:11px;color:var(--muted);white-space:nowrap}
.address{margin-left:auto;display:flex;gap:16px;font-size:10px;line-height:1.6;color:var(--text);margin-right:40px}
.address strong{color:var(--ink)}
.address .phone{color:var(--teal)}
</style>
</head>
<body>

<header class="site-header">
  <div class="brand"><span class="brand-dot"></span>Corvane</div>
  <nav class="main-nav">
    <a class="active" href="#">Home</a>
    <a href="#">About Us</a>
    <a href="#">Services</a>
    <a href="#">Pricing</a>
    <a href="#">Contact Us</a>
    <a class="btn-login" href="#">Login</a>
    <a class="btn-signup" href="#">Sign Up</a>
  </nav>
</header>

<section class="hero">
  <div class="hero-photo" role="img" aria-label="Photo of a smiling customer care team wearing headsets"></div>
  <div class="hero-content">
    <div class="brand"><span class="brand-dot"></span>Corvane</div>
    <p class="hero-lead">Corvane is an omnichannel provider for customer care and back-end office support.</p>
    <div class="hero-actions"><span class="btn-start">Get Started</span><span class="btn-more">Learn More</span></div>
  </div>
  <svg class="hero-wave" width="1200" height="60" viewBox="0 0 1200 60"><path d="M0 10 C200 35 380 38 560 25 C800 8 1000 20 1200 45 L1200 60 L0 60Z" fill="#fff"/></svg>
</section>

<section class="partners">
  <div class="partners-label"><b>Our Technology</b><br>Partners</div>
  <div class="partner-badges">
    <div class="partner-badge"><i></i></div>
    <div class="partner-badge"><i></i></div>
    <div class="partner-badge"><i></i></div>
    <div class="partner-badge"><i></i></div>
  </div>
</section>

<h2 class="services-title">OUR <b>SERVICES</b></h2>
<section class="services">
  <article class="service">
    <div class="service-icon"><svg width="48" height="42" viewBox="0 0 48 42"><rect x="2" y="2" width="44" height="30" rx="3" fill="none" stroke="#333" stroke-width="3"/><rect x="9" y="8" width="30" height="18" fill="none" stroke="#333" stroke-width="2"/><path d="M18 40h12M24 32v8" stroke="#333" stroke-width="3"/></svg></div>
    <h3>Digital Services</h3>
    <p>Lorem ipsum dolor sit amet, mel vis autem habemus recteque no. Ut per tota erant.</p>
    <span class="btn-outline">Learn More</span>
  </article>
  <article class="service">
    <div class="service-icon"><svg width="44" height="44" viewBox="0 0 48 46"><circle cx="24" cy="16" r="11" fill="#444"/><path d="M11 16a13 13 0 0 1 26 0" fill="none" stroke="#444" stroke-width="3"/><path d="M4 46c2-12 10-17 20-17s18 5 20 17Z" fill="#444"/></svg></div>
    <h3>Call Center Services</h3>
    <p>Lorem ipsum dolor sit amet, mel vis autem habemus recteque no. Ut per tota erant.</p>
    <span class="btn-outline">Learn More</span>
  </article>
</section>

<section class="faq">
  <svg class="faq-scallop" width="1200" height="24" viewBox="0 0 1200 24" preserveAspectRatio="none"><path d="M0 24 Q25 0 50 24 Q75 0 100 24 Q125 0 150 24 Q175 0 200 24 Q225 0 250 24 Q275 0 300 24 Q325 0 350 24 Q375 0 400 24 Q425 0 450 24 Q475 0 500 24 Q525 0 550 24 Q575 0 600 24 Q625 0 650 24 Q675 0 700 24 Q725 0 750 24 Q775 0 800 24 Q825 0 850 24 Q875 0 900 24 Q925 0 950 24 Q975 0 1000 24 Q1025 0 1050 24 Q1075 0 1100 24 Q1125 0 1150 24 Q1175 0 1200 24Z" fill="#f1f5f8"/></svg>
  <h2>Frequently Asked Questions</h2>
  <ul class="faq-list">
    <li class="faq-item open"><span>Is the free trial really free?</span><span class="sign">−</span>
      <p>The free trial only relates to the “call center” service packages! There is no hidden fine print or fees to get started. We don’t even require any payment info, signatures, or deposits. If you don’t like us or our service, just simply walk away.</p></li>
    <li class="faq-item"><span>Do I have to sign a contract?</span><span class="sign">+</span></li>
    <li class="faq-item"><span>Do I have to purchase any hardware or equipment?</span><span class="sign">+</span></li>
    <li class="faq-item"><span>Do you offer custom script writing?</span><span class="sign">+</span></li>
    <li class="faq-item"><span>I’m not sure how many minutes I’ll need?</span><span class="sign">+</span></li>
    <li class="faq-item"><span>Can I change my service plan?</span><span class="sign">+</span></li>
    <li class="faq-item"><span>Why do you use time-based billing over standard billing?</span><span class="sign">+</span></li>
    <li class="faq-item"><span>How long does it take to get started?</span><span class="sign">+</span></li>
  </ul>
</section>

<section class="contact">
  <h2>Get in Touch</h2>
  <div class="contact-rule"><i></i><b></b><i></i></div>
  <p class="contact-intro">Lorem ipsum dolor sit amet, consectetur adipisicing elit. Asperiores similique dolor ab inventore, veritatis deserunt suscipit vitae minima.</p>
  <div class="contact-form">
    <div class="field-row"><div class="field">Your Name</div><div class="field">Your E-Mail</div></div>
    <div class="field">Subject</div>
    <div class="field message">Your Message</div>
    <span class="btn-send">SEND MESSAGE</span>
  </div>
</section>

<footer class="site-footer">
  <div class="brand"><span class="brand-dot"></span>Corvane</div>
  <div class="copyright">© 2018. All Rights Reserved.</div>
  <div class="address">
    <svg width="16" height="22" viewBox="0 0 16 22"><path d="M8 0a8 8 0 0 0-8 8c0 6 8 14 8 14s8-8 8-14a8 8 0 0 0-8-8Z" fill="#4a4f50"/><circle cx="8" cy="8" r="3" fill="#fff"/></svg>
    <div><strong>Corvane, Inc.</strong><br>418 Larkmoor Ave.<br>Dunmere, CA 90412<br><span class="phone">(800) 555-0147</span></div>
  </div>
</footer>

</body>
</html>
```